Print on top the name of the company: (Or Similar)
Bellhaven Cleaning & Disinfecting
Because your standards aren't standard.

We adhere to ALL FHB guidelines for both residential and commercial cleaning.

Infection Control is our ultimate goal.

Instructions:
Opening a residential and commercial cleaning and disinfecting company in south Florida.

Targeting high-end residential clients, commercial and healthcare facilities, specializing in Ambulatory Care Guidelines. With a concentration and expertise in targeting Covid 19 and other transmissible pathogens.

TWLR trained.
Owned and operated by a licensed BSN Registered Nurse specially ​trained in Infection Control Prevention with over 25 years experience. Over two decades in Ambulatory Surgery Center Administration, Director of Nursing and Infection Control Prevention ad Consulting.

Looking to create a business flier that emphasizes Cleaning & Disinfection
along with the standard expectation for residential and Commercial cleaning services

Target Market(s)

Residential & Commercial

Font styles to use
Decorative

Requirements
Must have
• A checklist for cleaning services

```html
<!DOCTYPE html>
<html lang="en">
<head>
<meta charset="utf-8">
<title>Bellhaven Cleaning &amp; Disinfecting – Flyer</title>
<link href="https://fonts.googleapis.com/css2?family=Outfit:wght@600;700;800&family=Montserrat:wght@400;500&display=swap" rel="stylesheet">
<style>
  :root {
    --brand-blue: #1ba3e3;
    --brand-blue-deep: #243f9c;
    --band-blue: #1e9ad8;
    --ink: #1d1d1f;
    --paper: #ffffff;
    --paper-shade: #eef0f2;
    --stage: #bcbdbf;
    --photo-mid: #4b5b61;
    --badge-fill: #6a6e73;
  }
  * { margin: 0; padding: 0; box-sizing: border-box; }
  html, body { width: 999px; height: 1200px; overflow: hidden; background: var(--stage); }
  .flyer {
    position: absolute; left: 36px; top: 0;
    width: 844px; height: 1092px;
    transform: scale(1.0989); transform-origin: 0 0;
    background: linear-gradient(180deg, var(--paper) 0%, var(--paper) 60%, var(--paper-shade) 100%);
    overflow: hidden;
    font-family: "Montserrat", Arial, sans-serif;
    color: var(--ink);
  }
  .hero-shapes { position: absolute; left: 0; top: 0; width: 844px; height: 620px; }
  .logo-word {
    position: absolute; top: 20px; left: 0; width: 100%; text-align: center;
    font-family: "Outfit", Arial, sans-serif; font-weight: 700; font-size: 40px;
    letter-spacing: 1px; color: var(--brand-blue);
  }
  .headline {
    position: absolute; left: 61px; top: 180px;
    font-family: "Outfit", Arial, sans-serif; font-weight: 700;
    font-size: 49px; line-height: 52px; color: var(--paper);
    text-transform: uppercase;
  }
  .tagline {
    position: absolute; left: 61px; top: 344px;
    font-family: "Outfit", Arial, sans-serif; font-weight: 700;
    font-size: 28px; line-height: 31px; color: var(--brand-blue);
  }
  .badge { position: absolute; left: 64px; top: 425px; width: 122px; height: 104px; }
  .trained-title {
    position: absolute; left: 61px; top: 531px;
    font-family: "Outfit", Arial, sans-serif; font-weight: 700;
    font-size: 24px; color: var(--brand-blue);
  }
  .owner-note {
    position: absolute; left: 61px; top: 567px; width: 700px;
    font-size: 14px; line-height: 18px; color: var(--ink);
  }
  .service-card { position: absolute; top: 644px; width: 307px; }
  .service-card.commercial { left: 61px; }
  .service-card.residential { left: 466px; }
  .service-photo {
    height: 144px; border-radius: 12px 12px 0 0;
    background: linear-gradient(160deg, #3b4e63 0%, #6f9ac8 40%, #c9a76f 70%, #2d3a4a 100%);
  }
  .service-label {
    margin-top: -10px; height: 55px; border-radius: 0 0 12px 12px;
    border-top: 3px solid var(--paper);
    background: linear-gradient(90deg, var(--brand-blue) 0%, var(--brand-blue-deep) 100%);
    color: var(--paper); text-align: center;
    font-family: "Outfit", Arial, sans-serif; font-weight: 600;
    font-size: 23px; line-height: 52px; text-transform: uppercase;
  }
  .checklist { list-style: none; margin: 22px 0 0 27px; }
  .checklist li {
    display: flex; align-items: center; gap: 8px;
    font-size: 16.3px; line-height: 19.9px; color: var(--ink);
  }
  .checklist svg { width: 13px; height: 13px; flex: none; }
  .call-bar {
    position: absolute; left: 0; top: 1030px; width: 844px; height: 62px;
    background: linear-gradient(180deg, #27aee6 0%, var(--band-blue) 100%);
    display: flex; align-items: center; justify-content: center; gap: 16px;
    font-family: "Outfit", Arial, sans-serif; font-weight: 700;
    font-size: 34px; color: var(--paper);
  }
  .call-bar svg { width: 36px; height: 36px; }
</style>
</head>
<body>
  <div class="flyer">
    <svg class="hero-shapes" viewBox="0 0 844 620">
      <defs>
        <linearGradient id="bandGrad" x1="0" y1="0" x2="1" y2="0">
          <stop offset="0" stop-color="#1b8fd0"/>
          <stop offset="1" stop-color="#27aee6"/>
        </linearGradient>
        <linearGradient id="photoGrad" x1="0" y1="0" x2="1" y2="1">
          <stop offset="0" stop-color="#1f2a30"/>
          <stop offset="0.45" stop-color="#4b5b61"/>
          <stop offset="0.7" stop-color="#5a8fa8"/>
          <stop offset="1" stop-color="#2a3a42"/>
        </linearGradient>
      </defs>
      <polygon points="0,45 844,40 844,170 0,175" fill="url(#bandGrad)"/>
      <path d="M0,0 H844 V40 C800,80 780,118 700,120 C500,110 200,70 0,50 Z" fill="#ffffff"/>
      <path d="M0,50 C200,70 500,110 700,120 C760,122 790,95 844,40 L844,55 C800,100 770,132 700,134 C500,125 200,85 0,62 Z" fill="#e9ecef"/>
      <polygon role="img" aria-label="Photo: gloved hands spraying disinfectant and wiping a dark glass surface with a grey cloth"
        points="0,155 844,110 844,563 140,490 0,540" fill="url(#photoGrad)"/>
      <polygon points="0,540 140,490 844,563 844,575 140,502 0,555" fill="#dfe3e6"/>
      <polygon points="0,555 70,528 0,590" fill="#1b8fd0"/>
    </svg>

    <div class="logo-word">LOGO</div>

    <h1 class="headline">Bellhaven<br>Cleaning<br>&amp; Disinfecting</h1>
    <p class="tagline">Because your standards<br>aren't standard.</p>

    <svg class="badge" viewBox="0 0 122 104" role="img" aria-label="Certification badge placeholder">
      <circle cx="61" cy="52" r="50" fill="var(--badge-fill)"/>
    </svg>

    <h2 class="trained-title">TWLR TRAINED</h2>
    <p class="owner-note">Owned and operated by a licensed BSN Registered Nurse specially trained in Infection Control Prevention with over 25 years experience. Over two decades in Ambulatory Surgery Center Administration, Director of Nursing and Infection Control Prevention ad Consulting.</p>

    <section class="service-card commercial">
      <div class="service-photo" role="img" aria-label="Photo: glass office towers seen from street level against a blue sky"></div>
      <div class="service-label">Commercial</div>
      <ul class="checklist">
        <li><svg viewBox="0 0 14 14"><circle cx="7" cy="7" r="7" fill="#1a78c8"/><path d="M3.8 7.2 6 9.3 10.3 4.8" stroke="#fff" stroke-width="1.8" fill="none"/></svg>Janitorial</li>
        <li><svg viewBox="0 0 14 14"><circle cx="7" cy="7" r="7" fill="#1a78c8"/><path d="M3.8 7.2 6 9.3 10.3 4.8" stroke="#fff" stroke-width="1.8" fill="none"/></svg>Offices</li>
        <li><svg viewBox="0 0 14 14"><circle cx="7" cy="7" r="7" fill="#1a78c8"/><path d="M3.8 7.2 6 9.3 10.3 4.8" stroke="#fff" stroke-width="1.8" fill="none"/></svg>Floor maintenance</li>
        <li><svg viewBox="0 0 14 14"><circle cx="7" cy="7" r="7" fill="#1a78c8"/><path d="M3.8 7.2 6 9.3 10.3 4.8" stroke="#fff" stroke-width="1.8" fill="none"/></svg>Carpet cleaning</li>
        <li><svg viewBox="0 0 14 14"><circle cx="7" cy="7" r="7" fill="#1a78c8"/><path d="M3.8 7.2 6 9.3 10.3 4.8" stroke="#fff" stroke-width="1.8" fill="none"/></svg>Move-ins</li>
        <li><svg viewBox="0 0 14 14"><circle cx="7" cy="7" r="7" fill="#1a78c8"/><path d="M3.8 7.2 6 9.3 10.3 4.8" stroke="#fff" stroke-width="1.8" fill="none"/></svg>Move-outs</li>
        <li><svg viewBox="0 0 14 14"><circle cx="7" cy="7" r="7" fill="#1a78c8"/><path d="M3.8 7.2 6 9.3 10.3 4.8" stroke="#fff" stroke-width="1.8" fill="none"/></svg>Constructions clean-ups</li>
        <li><svg viewBox="0 0 14 14"><circle cx="7" cy="7" r="7" fill="#1a78c8"/><path d="M3.8 7.2 6 9.3 10.3 4.8" stroke="#fff" stroke-width="1.8" fill="none"/></svg>Estate clean-outs</li>
      </ul>
    </section>

    <section class="service-card residential">
      <div class="service-photo" role="img" aria-label="Photo: glass towers seen from street level against a blue sky"></div>
      <div class="service-label">Residential</div>
      <ul class="checklist">
        <li><svg viewBox="0 0 14 14"><circle cx="7" cy="7" r="7" fill="#1a78c8"/><path d="M3.8 7.2 6 9.3 10.3 4.8" stroke="#fff" stroke-width="1.8" fill="none"/></svg>House cleaning</li>
        <li><svg viewBox="0 0 14 14"><circle cx="7" cy="7" r="7" fill="#1a78c8"/><path d="M3.8 7.2 6 9.3 10.3 4.8" stroke="#fff" stroke-width="1.8" fill="none"/></svg>Before and after party</li>
        <li><svg viewBox="0 0 14 14"><circle cx="7" cy="7" r="7" fill="#1a78c8"/><path d="M3.8 7.2 6 9.3 10.3 4.8" stroke="#fff" stroke-width="1.8" fill="none"/></svg>Move-ins</li>
        <li><svg viewBox="0 0 14 14"><circle cx="7" cy="7" r="7" fill="#1a78c8"/><path d="M3.8 7.2 6 9.3 10.3 4.8" stroke="#fff" stroke-width="1.8" fill="none"/></svg>Move-outs</li>
        <li><svg viewBox="0 0 14 14"><circle cx="7" cy="7" r="7" fill="#1a78c8"/><path d="M3.8 7.2 6 9.3 10.3 4.8" stroke="#fff" stroke-width="1.8" fill="none"/></svg>Holiday cleaning</li>
        <li><svg viewBox="0 0 14 14"><circle cx="7" cy="7" r="7" fill="#1a78c8"/><path d="M3.8 7.2 6 9.3 10.3 4.8" stroke="#fff" stroke-width="1.8" fill="none"/></svg>Seasonal cleaing</li>
        <li><svg viewBox="0 0 14 14"><circle cx="7" cy="7" r="7" fill="#1a78c8"/><path d="M3.8 7.2 6 9.3 10.3 4.8" stroke="#fff" stroke-width="1.8" fill="none"/></svg>Carpet cleaning</li>
        <li><svg viewBox="0 0 14 14"><circle cx="7" cy="7" r="7" fill="#1a78c8"/><path d="M3.8 7.2 6 9.3 10.3 4.8" stroke="#fff" stroke-width="1.8" fill="none"/></svg>Deodorizing and sanitizing</li>
      </ul>
    </section>

    <div class="call-bar">
      <svg viewBox="0 0 36 36" aria-hidden="true">
        <circle cx="18" cy="18" r="17" fill="#fff"/>
        <path d="M12 10.5c1-.8 2-.6 2.6.4l1.5 2.6c.5.9.3 1.7-.5 2.3l-1 .7c.7 1.9 2.4 3.8 4.4 4.7l.8-1c.6-.8 1.5-.9 2.3-.4l2.5 1.6c1 .6 1.1 1.7.3 2.6l-1.3 1.4c-1 1-2.6 1.2-4.4.4-4.3-1.9-7.6-5.4-9.1-9.6-.6-1.8-.3-3.3.9-4.3z" fill="#1e9ad8"/>
      </svg>
      <span>CALL US NOW! (305) 555 0142</span>
    </div>
  </div>
</body>
</html>
```